Bionic Knee Brace Company Needs Brochure Design

Our revolutionary bionic knee braces do more than just stabilize your knee. Quorvanta's™ bionic hinge enhances your leg muscle power by storing energy as you bend your knee and returning that energy as you straighten your leg. The result is the world’s only compact and powerful bionic knee brace capable of boosting strength, mobility, and performance.

We need a double sided one page patient resource made for topics such as ACL injury treatment, osteoarthritis pre-operative care, and osteoarthritis post-operative care.

We are looking for designs that are broadly consistent with the look and feel of our website, product one pager, eBook and other resources. The copy for three different resources are included as attachments.

Please refer to our website for more information about our company and brand: https://brindlecoremedical.example/
Updates

Font styles to use
Sans Serif

Colors
0355a3
0492cd

Requirements
Must have
• -One pagers must be created using Adobe InDesign. The final deliverable is the .indd file.
• -Width: 8.5 in, Height: 11 in
• -Intent: print/web
• -Orientation: portrait
• -Number of pages: 2
• Proxima Nova is the official font of Brindle Core Medical
• The official blue (including in the logo) for Brindle Core Medical is #2075c0.
• Brindle Core Medical has a secondary color, which is dark blue.
• The official dark blue for Brindle Core Medical is # 195a94.
• Brindle Core Medical has a tertiary color, which is yellow.
• The official yellow for Brindle Core Medical is # ffb218.
• Brindle Core Medical has a quaternary color, which is dark grey.
• The official dark grey for Brindle Core Medical is #4c4c4c.
Nice to have
• Ideally, the one pager would be easily changed to accommodate different copy for different resources.

```html
<!DOCTYPE html>
<html lang="en">
<head>
<meta charset="utf-8">
<title>Brindle Core Medical – ACL Patient Resource</title>
<link href="https://fonts.googleapis.com/css2?family=Source+Sans+3:wght@400;600;700&display=swap" rel="stylesheet">
<style>
  :root {
    --canvas-bg: #e4e6ea;
    --page-top: #d6e1ef;
    --page-bottom: #eef2f8;
    --ink: #1f2329;
    --ink-soft: #2e333a;
    --brand-blue: #2075c0;
    --footer-dark: #2b3138;
    --footer-slate: #5a6e93;
    --footer-text: #e9edf3;
    --photo-a: #6f6d6a;
    --photo-b: #c9c3b8;
    --diagram-a: #f4ead8;
    --diagram-b: #b9d8ea;
  }
  * { box-sizing: border-box; margin: 0; padding: 0; }
  html, body { width: 1200px; height: 750px; overflow: hidden; }
  body {
    background: var(--canvas-bg);
    font-family: "Source Sans 3", sans-serif;
    color: var(--ink);
    position: relative;
  }
  .page {
    position: absolute;
    top: 46px;
    width: 512px;
    height: 663px;
    background: linear-gradient(170deg, var(--page-top) 0%, var(--page-bottom) 70%, #e3e9f2 100%);
    box-shadow: 0 2px 10px rgba(0,0,0,0.18);
    overflow: hidden;
  }
  .page--front { left: 66px; }
  .page--back { left: 624px; }
  .block { position: absolute; line-height: 12px; font-size: 9.5px; color: var(--ink-soft); }

  /* Front page */
  .doc-title { left: 35px; top: 42px; font-size: 11.5px; color: var(--ink); }
  .doc-function { left: 35px; top: 58px; font-size: 9px; }
  .col-head { font-size: 11px; color: var(--ink); margin-bottom: 5px; }
  .causes { left: 39px; top: 76px; }
  .symptoms { left: 244px; top: 76px; }
  .note { left: 39px; top: 163px; width: 440px; font-size: 9px; }
  .factors { left: 130px; width: 240px; top: 228px; text-align: center; font-size: 11.5px; line-height: 15px; color: var(--ink); }
  .diag-head { left: 39px; top: 291px; font-weight: 600; font-size: 9px; color: var(--ink); }
  .diag-text { left: 150px; top: 306px; font-size: 9px; }
  .scale-head { left: 39px; top: 337px; font-size: 9px; }
  .grade { top: 364px; font-size: 9px; }
  .grade h3 { font-size: 9.5px; font-weight: 600; color: var(--ink); margin-bottom: 5px; line-height: 12px; }
  .grade--1 { left: 39px; }
  .grade--2 { left: 204px; }
  .grade--3 { left: 337px; width: 140px; }
  .exam { left: 39px; top: 441px; width: 440px; font-size: 9px; }
  .imaging { left: 39px; top: 489px; width: 440px; font-size: 9px; }

  .footer-shape { position: absolute; left: 0; top: 551px; }
  .footer-label { left: 42px; top: 585px; font-size: 7px; color: var(--footer-text); letter-spacing: 0.2px; }
  .footer-contact { top: 605px; font-size: 7px; line-height: 10px; color: var(--footer-text); }
  .footer-contact--left { left: 42px; }
  .footer-contact--right { left: 139px; }
  .brand-name { display: flex; align-items: center; gap: 6px; font-weight: 700; white-space: nowrap; }
  .brand-dot { width: 10px; height: 10px; border-radius: 50%; background: currentColor; }
  .footer-brand { left: 333px; top: 589px; font-size: 12.5px; color: #ffffff; }
  .footer-url { left: 364px; top: 623px; font-size: 7px; color: var(--footer-text); }

  /* Back page */
  .tagline { right: 54px; top: 57px; font-size: 8.5px; letter-spacing: 0.2px; color: var(--ink-soft); }
  .header-brand { right: 54px; top: 78px; font-size: 17px; color: var(--brand-blue); line-height: 20px; }
  .header-brand .brand-dot { width: 16px; height: 16px; }
  .photo { position: absolute; left: 54px; top: 128px; width: 404px; height: 220px;
    background: linear-gradient(120deg, var(--photo-a) 0%, #a9a49b 45%, var(--photo-b) 100%); }
  .resource-title { left: 50px; top: 364px; font-size: 10px; font-weight: 700; color: var(--ink); }
  .resource-credit { left: 50px; top: 377px; font-size: 7.5px; }
  .anatomy { left: 50px; top: 392px; font-size: 10px; color: var(--ink); }
  .copy { left: 50px; width: 240px; font-size: 7.3px; line-height: 9.8px; }
  .copy ul { list-style: none; }
  .copy li { position: relative; padding-left: 11px; }
  .copy li::before { content: ""; position: absolute; left: 1px; top: 3px; width: 4px; height: 4px; border-radius: 50%; background: var(--ink); }
  .copy h3 { font-size: 7.5px; font-weight: 700; color: var(--ink); line-height: 10px; }
  .copy h3.large { font-size: 9px; margin-bottom: 1px; }
  .copy strong { font-weight: 700; }
  .bones { top: 409px; }
  .collateral { top: 436px; }
  .collateral ul { margin-top: 12px; line-height: 11px; }
  .cruciate { top: 501px; }
  .cruciate ul { margin-top: 10px; }
  .cruciate li + li { margin-top: 2px; }
  .diagram { position: absolute; left: 310px; top: 394px; width: 138px; height: 175px;
    background: #ffffff; padding: 6px; box-shadow: 0 0 2px rgba(0,0,0,0.1); }
  .diagram-fill { width: 100%; height: 100%;
    background: linear-gradient(180deg, var(--diagram-a) 0%, var(--diagram-b) 55%, var(--diagram-a) 100%); }
</style>
</head>
<body>

<section class="page page--front">
  <h1 class="block doc-title" style="font-weight:400">The Anterior Cruciate Ligament (ACL)</h1>
  <p class="block doc-function">Primary Function: To prevent the shinbone from excessive forward movement.</p>

  <div class="block causes">
    <h2 class="col-head" style="font-weight:400">Causes:</h2>
    <p>Sudden change in direction*<br>Abrupt stop or slowing down*<br>Improper landing from a jump*<br>Direct contact or collision</p>
  </div>
  <div class="block symptoms">
    <h2 class="col-head" style="font-weight:400">Symptoms:</h2>
    <p>Pain and Swelling<br>Apparent instability of the knee joint<br>Tenderness in and around the knee<br>Inability or discomfort while walking</p>
  </div>

  <p class="block note">*Non-Contact injuries (injuries that do not occur from direct contact or a blow to the knee joint) account for 70-80% of all ACL injuries<br>Studies show that teenage and adult females may be 2-8x more likely to experience a non-contact ACL injury compared to males for a variety of proposed differences<br>variety of proposed differences2</p>

  <p class="block factors">Muscular strength<br>Neuromuscular coordination and control<br>Pelvic and leg alignment<br>Hormones</p>

  <h2 class="block diag-head">Injury Diagnosis</h2>
  <p class="block diag-text">Ligament damage is referred to as a sprain</p>
  <p class="block scale-head">Sprain Severity Scale</p>

  <div class="block grade grade--1"><h3>Grade 1</h3><p>-Mild Damage<br>-Still able to keep joint stable</p></div>
  <div class="block grade grade--2"><h3>Grade 2</h3><p>-Partial tear of the ligament<br>-Ligament becomes stretched</p></div>
  <div class="block grade grade--3"><h3>Grade 2</h3><p>-Complete tear<br>-Knee joint becomes unstable<br>*Majority of ACL injuries are complete or severe tears</p></div>

  <p class="block exam">Physical Examination 1<br>Your doctor is likely able to diagnose an ACL injury using a physical examination that tests the structures of your injured knee compared to your non-injured knee</p>
  <p class="block imaging">Imaging1<br>Your doctor may confirm a diagnosis using:<br>MRI Scan – used to image soft tissue structure such as ligaments, tendons and muscles<br>X-Ray – May be used to check for associated fractures or broken bones.</p>

  <svg class="footer-shape" width="512" height="112" viewBox="0 0 512 112" aria-hidden="true">
    <polygon points="0,21 310,21 309,0 512,0 512,112 0,112" fill="var(--footer-dark)"/>
    <polygon points="252,21 270,0 512,0 512,112 310,112 242,21" fill="var(--footer-slate)"/>
  </svg>
  <p class="block footer-label">ORDERS AND INQUIRIES:</p>
  <p class="block footer-contact footer-contact--left">1.800.555.0142<br>Port Averly, Nova Scotia<br>Canada</p>
  <p class="block footer-contact footer-contact--right">kneehelp.example<br>updates.brindlecoremedical.example<br>community.brindlecoremedical.example</p>
  <div class="block footer-brand brand-name"><span class="brand-dot"></span>Brindle Core Medical</div>
  <p class="block footer-url">brindlecoremedical.example</p>
</section>

<section class="page page--back">
  <p class="block tagline">DO MORE OF WHAT YOU LOVE</p>
  <div class="block header-brand brand-name"><span class="brand-dot"></span>Brindle Core Medical</div>

  <div class="photo" role="img" aria-label="Photo of a man in a grey sweater sitting on a sunlit wooden floor wearing a knee brace"></div>

  <h2 class="block resource-title">Brindle Core Medical Patient Resource -ACL Injuries</h2>
  <p class="block resource-credit">Information prepared by Daniel Roesch</p>
  <h3 class="block anatomy" style="font-weight:400">Anatomy of the Knee Joint</h3>

  <div class="block copy bones">
    <ul><li>Thighbone, shinbone and kneecap form the knee joint</li><li>The bones are connected by 4 main ligaments:</li></ul>
  </div>
  <div class="block copy collateral">
    <h3>Collateral Ligaments:</h3>
    <p>These ligaments stabilize against side-to-side motion of the knee</p>
    <ul><li>Medial Collateral Ligament (MCL) - Inside of the knee</li><li>Lateral Collateral Ligament (LCL) - Outside of the knee</li></ul>
  </div>
  <div class="block copy cruciate">
    <h3 class="large">Cruciate Ligaments:</h3>
    <p>These ligaments are inside the joint and cross each other, forming an 'x'. As a result, these ligaments are able to stabilize against excessive forwards and backwards motion of the knee.</p>
    <ul>
      <li><strong>Anterior Cruciate Ligament</strong> – Attached from the front of the shinbone to the back of the thighbone.</li>
      <li><strong>Posterior Cruciate Ligament</strong> – Attached from the back of the shinbone to the front of the thighbone.</li>
    </ul>
  </div>

  <div class="diagram">
    <div class="diagram-fill" role="img" aria-label="Labelled anatomical illustration of the knee joint showing femur, patella, tibia, fibula and the collateral and cruciate ligaments"></div>
  </div>
</section>

</body>
</html>
```